Successful Health Company Needs a Face Lift

We need a beautiful new design for our existing, online health supplements business.

Most of the elements are already there, but we need your sophistication and style.

The 3 pages that need your magic touch are:
Home page:
http://www.vitabrook.co.uk

Multiple Product pages. e.g:
http://www.vitabrook.co.uk/health-issues/major-organs/skin-hair-nails.html

Single Product pages. e.g:
http://www.vitabrook.co.uk/l-arginine-500-mg.html

Please have a look around.

This is a bilingual site, so all text (except logo) needs to be easily changed/translated. If photoshop files can be provided where we can simply translate the text layer of a graphic, that is acceptable. Please note that Greman words are generally longer than English.

Appearance:
The over all look should be open, light, uplifting and sophisticated.

The Home Page in detail:
We are largely happy with the category boxes in the centre column although you may restyle these if you wish.
The header, left menu and right column don't hang together and need your skills.

Logo:
We would like you to enhance our logo, but please note the 'S' and circle are used on many product labels, so we can't go too far from this just now.
(Product label example: http://www.vitabrook.co.uk/black-walnut-tincture-from-green-hull.html)

Header:
This needs to imply health and be light and stylish without it taking up valuable room.

Left Menu:
This is a multi-layer concertina menu. It is hard to see where your are within it. It needs to be made more clear and easy to navigate, maybe by using indentation and or better colour choices.
Please show it expanded and condensed in your design proposals.
(Extended menu example: http://www.vitabrook.co.uk/health-issues/female-health/thrush.html)

Multiple Product pages in detail
Please style the the brief descriptions, which must contain bullet points, price, add to basket and learn more.

Single Product pages in detail
The design and layout of this page needs to include all the elements currently there, including price, Qty, Add to Basket button, size and article number.

The static blocks on the right column will appear on these single product pages and need to suit the design well. They should not over-power the central content of the page.
Updates

Thank you all for participating.

Please note that what we are looking for is a more stylish and attractive version of what we already have.  The elements are all there.  We are not looking for a new concept.

We are happy for designers to switch images for better ones, work with colour ways, alter proportions and insert the elements in our brief.

We do not want to add banners, large images etc.  We want our customers to be familiar with what they see, and to be impressed with how much better the pages hang together.  They should not think they've landed at a new company.

We do want to see how the left menu looks when extended to show 2nd and 3rd tier menu titles.
We will also want to see how the design works for a multiple product page like this: http://www.vitabrook.co.uk/supplement-type/anti-microbials.html
as well as a single product page like this:  http://www.vitabrook.co.uk/black-walnut-extract.html

Some adjustment to the 'VitaBrook' logo is also an option and the graphic has been attached. 

Thank you for your careful attention to our brief.

Marcus.
pp Leopold

Project Deadline Extended
Reason: Due to unanticipated travel arrangements, the company director will only be available to make final decisions on Monday the 19th of March. Please continue updating submissions as we are in touch. Thank you for your understanding.

Target Market(s)

Health conscious women 70% men 30% aged 40 to 65 and health practitioners.

Industry/Entity Type

Health

Requirements
Must have
• Please include in the Header:
UK and German flags
Facebook, dig, +1, twitter, linked in, stumble upon
Padlock/SSL security/secure transaction
Practitioner helpline/ orders phone number
Paypal/Credit card logo

Please include in right column:
Clinician Corner
Mercury Free Dentistry
Shopping Basket
Storefronts for Therapists

Please include in either Header or Right Column
Same day dispatch
Money back warranty

```html
<!DOCTYPE html>
<html lang="en">
<head>
<meta charset="utf-8">
<title>VitaBrook Enterprises – Natural Health Supplements</title>
<link href="https://fonts.googleapis.com/css2?family=Open+Sans:wght@300;400;600;700&family=Oswald:wght@400;500&display=swap" rel="stylesheet">
<style>
:root{
  --pink:#e3166a;
  --pink-soft:#e56a9a;
  --blue:#7fb3d5;
  --blue-dark:#2a9fd0;
  --brand:#86c3e2;
  --teal:#1a8fb5;
  --ink:#333;
  --grey:#666;
  --line:#dcdcdc;
  --panel:#f2f2f2;
  --white:#fff;
  --olive:#6f6a2a;
  --red:#c8102e;
}
*{margin:0;padding:0;box-sizing:border-box}
html,body{width:1000px;height:1200px;overflow:hidden;background:var(--white)}
body{position:relative;font-family:"Open Sans",Arial,sans-serif;color:var(--ink);font-size:11px}
.abs{position:absolute}
ul{list-style:none}

/* brand */
.brand-mark{left:22px;top:16px;width:68px;height:68px;border-radius:50%;border:4px solid var(--brand)}
.brand-name{left:106px;top:14px;font-size:38px;font-weight:300;letter-spacing:1px;color:var(--brand);line-height:44px}
.brand-sub{left:284px;top:53px;font-size:10px;letter-spacing:2px;color:var(--brand)}

/* utility bar */
.util-rule{left:598px;top:38px;width:382px;height:1px;background:var(--line)}
.util-div{top:0;width:1px;height:38px;background:var(--line)}
.flag{top:9px;width:22px;height:15px}
.login{left:692px;top:10px;font-size:11px;color:var(--grey)}
.social{top:7px;width:20px;height:20px;border-radius:3px}
.plus-one{left:920px;top:8px;width:30px;height:17px;border:1px solid #ccc;border-radius:3px;font-size:10px;font-weight:700;text-align:center;line-height:15px;color:var(--grey)}
.count{left:957px;top:8px;width:22px;height:17px;border:1px solid #ccc;border-radius:3px;font-size:10px;text-align:center;line-height:15px;color:var(--grey)}

.cart-icon{left:778px;top:55px}
.cart-title{left:809px;top:52px;font-size:15px;color:var(--pink)}
.cart-note{left:810px;top:75px;font-size:11px;color:var(--grey)}
.cart-link{left:810px;top:94px;font-size:10px;color:var(--pink)}

/* main nav */
.nav-tab{top:119px;height:38px;background:var(--blue);color:var(--white);font-weight:700;font-size:14px;line-height:38px;padding-left:10px;border-radius:4px 26px 0 0}
.search-shell{left:700px;top:119px;width:280px;height:38px;background:linear-gradient(#f7f7f7,#e9e9e9);border:1px solid var(--line);border-bottom:0;border-radius:30px 4px 0 0}
.search-box{left:741px;top:128px;width:232px;height:22px;border:1px solid #ccc;border-radius:11px;background:var(--white);font-size:12px;line-height:20px;padding-left:8px;color:var(--grey)}
.search-btn{left:954px;top:131px;width:16px;height:16px;border-radius:4px;background:var(--pink-soft)}

/* trust bar */
.trust{left:22px;top:157px;width:958px;height:74px;border:1px solid var(--line);background:linear-gradient(#fff,#efefef)}
.trust-div{top:157px;width:1px;height:74px;background:var(--line)}
.secure{left:84px;top:170px;font-size:15.5px;letter-spacing:-.3px;color:var(--grey);white-space:nowrap}
.secure b{color:var(--pink);font-weight:700}
.card{top:195px;width:31px;height:20px;border-radius:3px;border:1px solid #bbb}
.helpline{left:331px;width:317px;top:167px;text-align:center;font-size:13px;color:var(--grey);white-space:nowrap}
.phone{left:331px;width:317px;top:183px;text-align:center;font-size:30px;color:var(--blue-dark)}
.badge{left:668px;top:169px;width:48px;height:48px;border-radius:50%;background:radial-gradient(#f4d03f,#b8860b)}
.perk{font-family:"Oswald",sans-serif;font-size:18px;color:var(--grey);line-height:19px}
.perk small{display:block;font-family:"Open Sans",sans-serif;font-size:11px;font-weight:600}

/* left sidebar */
.sidebar{left:22px;top:240px;width:185px;height:520px;background:var(--panel)}
.menu{left:31px;top:250px;width:166px;background:var(--white)}
.menu li{height:29.4px;line-height:29px;padding-left:9px;font-size:11px;border-bottom:1px dashed #ccc;position:relative}
.menu li.active{color:var(--pink)}
.menu li.more::after{content:"+";position:absolute;right:10px;top:0;color:var(--pink);font-size:17px;font-weight:400}
.news-pre{left:32px;top:643px;font-size:19px;font-weight:300;color:var(--grey)}
.news-title{left:32px;top:658px;font-size:27px;font-weight:400;color:var(--blue)}
.news-input{left:32px;top:694px;width:165px;height:24px;border:1px solid #ccc;background:var(--white);font-size:11px;line-height:22px;padding-left:5px}
.news-btn{left:33px;top:725px;width:59px;height:23px;border-radius:6px;background:var(--blue);color:var(--white);font-weight:700;font-size:11px;text-align:center;line-height:23px}

/* category boxes */
.cat{width:274px;height:126px;border:1px solid var(--line);background:var(--white);overflow:hidden}
.cat h3{position:absolute;left:10px;top:7px;font-size:13px;color:var(--pink);font-weight:700}
.cat ul{position:absolute;left:10px;top:30px}
.cat li{font-size:11px;line-height:17.6px;padding-left:8px;position:relative}
.cat li::before{content:"";position:absolute;left:0;top:6px;border-left:4px solid var(--pink);border-top:3px solid transparent;border-bottom:3px solid transparent}
.cat li.plain::before{display:none}
.cat-art{position:absolute;right:0;top:0;width:150px;height:100%}

/* right column */
.rc-title{left:793px;font-family:"Oswald",sans-serif;font-size:17.5px;font-weight:500;color:#444;white-space:nowrap}
.rc-block{left:793px;width:187px}
.hub-text{left:793px;top:262px;width:82px;height:128px;background:var(--olive);color:var(--white);font-size:14px;line-height:16px;padding:8px 5px}
.dent-text{left:797px;top:438px;font-size:14px;line-height:16px;color:#555}
.dent-text b{font-weight:400;color:var(--blue-dark)}
.basket-text{left:800px;top:588px;width:108px;font-size:13px;line-height:15px;color:var(--red)}
.store{left:793px;top:665px;width:187px;height:230px;border:1px solid var(--line)}
.store-name{left:793px;width:187px;top:812px;text-align:center;color:var(--teal);line-height:26px}

/* footer */
.footer{left:22px;top:983px;width:958px;height:148px;background:#f4f4f4;border:1px solid var(--line);border-radius:6px}
.foot-col{top:997px}
.foot-col li{font-size:11px;line-height:20.6px;color:var(--teal);padding-left:7px;position:relative}
.foot-col li::before{content:"";position:absolute;left:0;top:9px;width:3px;height:3px;background:#aaa}
.foot-links{left:22px;width:958px;top:1098px;text-align:center;font-size:11px;color:var(--ink)}
.foot-links span{margin:0 6px}
.base-rule{left:0;top:1163px;width:1000px;height:1px;background:#cfe0e8}
.base-mark{left:31px;top:1141px;width:46px;height:46px;border-radius:50%;border:3px solid var(--brand);background:var(--white)}
.copyright{left:90px;top:1156px;background:var(--white);padding:0 7px;font-size:11px;color:var(--ink)}
</style>
</head>
<body>

<!-- Brand -->
<div class="abs brand-mark"></div>
<div class="abs brand-name">VITABROOK</div>
<div class="abs brand-sub">ENTERPRISES</div>

<!-- Utility bar -->
<div class="abs util-rule"></div>
<svg class="abs flag" style="left:613px" viewBox="0 0 22 15" role="img" aria-label="German language">
  <rect width="22" height="5" fill="#000"/><rect y="5" width="22" height="5" fill="#d00"/><rect y="10" width="22" height="5" fill="#fc0"/>
</svg>
<svg class="abs flag" style="left:639px" viewBox="0 0 22 15" role="img" aria-label="English language">
  <rect width="22" height="15" fill="#012169"/>
  <path d="M0 0L22 15M22 0L0 15" stroke="#fff" stroke-width="3"/>
  <path d="M0 0L22 15M22 0L0 15" stroke="#c8102e" stroke-width="1"/>
  <path d="M11 0V15M0 7.5H22" stroke="#fff" stroke-width="5"/>
  <path d="M11 0V15M0 7.5H22" stroke="#c8102e" stroke-width="3"/>
</svg>
<div class="abs util-div" style="left:677px"></div>
<div class="abs login">Login &nbsp;|&nbsp; Registe</div>
<div class="abs util-div" style="left:786px"></div>
<div class="abs social" style="left:801px;background:#5bc0de"></div>
<div class="abs social" style="left:825px;background:#3b5998"></div>
<div class="abs social" style="left:849px;background:#3a9a4e"></div>
<div class="abs social" style="left:873px;background:#0e76a8"></div>
<div class="abs social" style="left:896px;background:#2f66a3"></div>
<div class="abs plus-one">+1</div>
<div class="abs count">2</div>

<!-- Cart -->
<svg class="abs cart-icon" width="26" height="22" viewBox="0 0 26 22" aria-hidden="true">
  <path d="M1 2h4l3 12h13l3-9H7" fill="none" stroke="#aaa" stroke-width="2"/>
  <circle cx="10" cy="18" r="2" fill="#aaa"/><circle cx="19" cy="18" r="2" fill="#aaa"/>
</svg>
<div class="abs cart-title">Shopping Cart</div>
<div class="abs cart-note">Your cart is currently empty</div>
<div class="abs cart-link">VIEW CART ▸</div>

<!-- Main navigation -->
<div class="abs nav-tab" style="left:22px;width:83px">HOME</div>
<div class="abs nav-tab" style="left:108px;width:85px">DETOX</div>
<div class="abs nav-tab" style="left:194px;width:124px">HYDRATION</div>
<div class="abs nav-tab" style="left:321px;width:145px">SUPPLEMENTS</div>
<div class="abs nav-tab" style="left:469px;width:201px">YOUR HEALTH ISSUES</div>
<div class="abs search-shell"></div>
<div class="abs search-box">Search</div>
<div class="abs search-btn"></div>

<!-- Trust bar -->
<div class="abs trust"></div>
<svg class="abs" style="left:35px;top:166px" width="40" height="52" viewBox="0 0 40 52" aria-hidden="true">
  <path d="M10 22V14a10 10 0 0 1 20 0v8" fill="none" stroke="#999" stroke-width="5"/>
  <rect x="3" y="22" width="34" height="28" rx="4" fill="#e8b320"/>
  <circle cx="20" cy="34" r="3" fill="#7a5a00"/><rect x="19" y="35" width="2" height="7" fill="#7a5a00"/>
</svg>
<div class="abs secure"><b>100% SECURE</b> FOUNDED 1996</div>
<div class="abs card" style="left:86px;background:#1a1f71"></div>
<div class="abs card" style="left:126px;background:#f79e1b"></div>
<div class="abs card" style="left:166px;background:#2e77bb"></div>
<div class="abs card" style="left:206px;background:#eef2f7"></div>
<div class="abs card" style="left:245px;background:#cc2a3a"></div>
<div class="abs trust-div" style="left:330px"></div>
<div class="abs helpline">Practitioner Helpline &nbsp;/ Orders Phone Number</div>
<div class="abs phone">01632 960 418</div>
<div class="abs trust-div" style="left:648px"></div>
<div class="abs badge"></div>
<div class="abs perk" style="left:724px;top:176px">MONEY BACK<small>100% GUARANTEE</small></div>
<svg class="abs" style="left:839px;top:180px" width="44" height="30" viewBox="0 0 44 30" aria-hidden="true">
  <rect x="0" y="3" width="28" height="18" fill="#3a8fd0"/>
  <path d="M28 8h9l6 7v6H28z" fill="#3a8fd0"/>
  <circle cx="9" cy="24" r="4" fill="#555"/><circle cx="35" cy="24" r="4" fill="#555"/>
</svg>
<div class="abs perk" style="left:890px;top:174px">SAME DAY<br>DISPATCH</div>

<!-- Left sidebar -->
<div class="abs sidebar"></div>
<ul class="abs menu">
  <li class="active">A to Z</li>
  <li class="more">Supplement Type</li>
  <li class="more">Your Health Issue</li>
  <li class="more">Expert Product Lines</li>
  <li class="more">Detox &amp; Cleansing</li>
  <li class="more">Hydration &amp; Water</li>
  <li class="more">Natural Body Care</li>
  <li>Sport &amp; Fitness</li>
  <li>Health Technology</li>
  <li>Household Products</li>
  <li>Laboratory Tests</li>
  <li>Books &amp; Education</li>
  <li>New &amp; Special Offers</li>
</ul>
<div class="abs news-pre">SIGN UP FOR OUR</div>
<div class="abs news-title">NEWSLETTER</div>
<div class="abs news-input">Your email address</div>
<div class="abs news-btn">SIGN UP</div>

<!-- Category boxes -->
<div class="abs cat" style="left:217px;top:240px">
  <div class="cat-art" role="img" aria-label="Photo of hands forming a heart over a stomach" style="background:linear-gradient(90deg,#fff,#ead7cc 40%,#e2c4b4)"></div>
  <h3>Digestion</h3>
  <ul><li>Constipation</li><li>Candida</li><li>Irritable Bowel</li><li>Wind</li></ul>
</div>
<div class="abs cat" style="left:509px;top:240px">
  <div class="cat-art" role="img" aria-label="Photo of a man holding his aching back" style="width:170px;background:linear-gradient(90deg,#fff,#d9d9d9 40%,#bdbdbd 80%,#d88)"></div>
  <h3>Pain</h3>
  <ul><li>Back Pain</li><li>Joint and Bone</li><li>Headaches</li><li>Period Pain</li></ul>
</div>
<div class="abs cat" style="left:217px;top:385px">
  <div class="cat-art" role="img" aria-label="Photo of a slim waist with a measuring tape" style="width:140px;background:linear-gradient(90deg,#fff,#c89a78 35%,#8a5a3e 70%,#2a2a2a)"></div>
  <h3>Weight Loss</h3>
  <ul><li>Without Dieting</li><li>Supplements</li><li>Sugar Metabolism</li></ul>
</div>
<div class="abs cat" style="left:509px;top:385px">
  <div class="cat-art" role="img" aria-label="Illustration of male and female symbols" style="left:96px;width:70px;background:radial-gradient(circle at 45% 50%,#8ab6e6,#e49ac4 55%,#fff 75%)"></div>
  <h3>Female Health</h3>
  <ul><li>Constipation</li><li>Candida</li><li>Irritable Bowel</li><li>Wind</li></ul>
  <h3 style="left:174px">Male Health</h3>
  <ul style="left:174px"><li>Back Pain</li><li>Joint and Bone</li><li>Headaches</li><li>Period Pain</li></ul>
</div>
<div class="abs cat" style="left:217px;top:528px">
  <div class="cat-art" role="img" aria-label="Illustration of a human heart" style="width:120px;background:radial-gradient(ellipse at 45% 55%,#a52a2a,#7a1a1a 40%,#fff 70%)"></div>
  <h3>Cardiovascular</h3>
  <ul><li>Blood Pressure</li><li>Cholesterol</li><li>Heart &amp; Arteries</li></ul>
</div>
<div class="abs cat" style="left:509px;top:528px">
  <div class="cat-art" role="img" aria-label="Illustration of a stethoscope forming a cross" style="width:130px;background:radial-gradient(ellipse at 55% 55%,#f3dede,#fff 70%)"></div>
  <h3>Health Devices</h3>
  <ul><li>Zapping</li><li>Cardiovascular</li><li>Ozone</li><li>Allergy Test</li></ul>
</div>
<div class="abs cat" style="left:217px;top:672px">
  <div class="cat-art" role="img" aria-label="Illustration of a brain with a stethoscope" style="width:140px;background:radial-gradient(ellipse at 50% 40%,#c9876c,#e7c3b2 40%,#fff 70%)"></div>
  <h3>Brain Health</h3>
  <ul><li>Memory</li><li>Headaches</li><li>Cognitive Function</li><li class="plain">Mood &amp; Sleep</li></ul>
</div>
<div class="abs cat" style="left:509px;top:672px">
  <div class="cat-art" role="img" aria-label="Photo of a water splash" style="width:160px;background:radial-gradient(ellipse at 60% 70%,#7fc4e8,#d6eef9 45%,#fff 75%)"></div>
  <h3>Water &amp; Hydration</h3>
  <ul><li>Water Filtration</li><li>Electrolytes</li><li>Super-Hydration</li><li>&nbsp;</li></ul>
</div>
<div class="abs cat" style="left:217px;top:816px">
  <div class="cat-art" role="img" aria-label="Photo of a woman's legs" style="width:200px;background:linear-gradient(90deg,rgba(255,255,255,0),#ecd6c8 40%,#e4c3ae 75%,#f7f1ec)"></div>
  <h3>Body Care</h3>
  <ul><li>Anti Aging</li><li>Cosmetics</li><li>Skin Range</li><li>Face &amp; Mouth</li><li>Hair Care</li></ul>
</div>
<div class="abs cat" style="left:509px;top:816px">
  <div class="cat-art" role="img" aria-label="Photo of fresh wheatgrass" style="width:155px;background:linear-gradient(0deg,#3f8a1e,#7ec23a 50%,#fff)"></div>
  <h3>Detox</h3>
  <ul><li>Heavy Metal Detox</li><li>Parasite Cleanse</li><li>Kidney Cleanse</li><li>Liver Cleanse</li><li>Colon Cleanse</li></ul>
</div>

<!-- Right column -->
<div class="abs rc-title" style="top:235px">CLINICIAN CORNER</div>
<div class="abs rc-block" style="top:262px;height:128px;background:linear-gradient(90deg,#6f6a2a,#a39a4a 40%,#d9c7a8 75%,#efe6d6)" role="img" aria-label="Photo of a smiling natural health practitioner"></div>
<div class="abs hub-text">Contact a Natural Health Practitioner</div>

<div class="abs rc-title" style="top:405px">MERCURY FREE DENTISTRY</div>
<div class="abs rc-block" style="top:431px;height:106px;background:linear-gradient(90deg,#fff 20%,#f1d9d2 50%,#d99a92 80%,#c77f7a)" role="img" aria-label="Photo of a dental check-up"></div>
<div class="abs dent-text">A<br>comprehensive<br>list<br><b>available<br>here.</b></div>

<div class="abs rc-title" style="top:552px">SHOPPING BASKET</div>
<div class="abs rc-block" style="top:578px;height:73px;background:#f3e9ea"></div>
<div class="abs basket-text">You have no items in your shopping basket.</div>
<div class="abs" style="left:906px;top:584px;width:66px;height:60px;background:radial-gradient(ellipse at 50% 60%,#d32020,#e87a7a 50%,#f3e9ea 75%)" role="img" aria-label="Illustration of a red shopping basket"></div>

<div class="abs store"></div>
<div class="abs" style="left:803px;top:672px;width:167px;height:135px;background:radial-gradient(ellipse at 50% 50%,#c62828,#e7a3a3 35%,#e6e6e6 55%,#fff 75%)" role="img" aria-label="Illustration of a laptop showing an online storefront"></div>
<div class="abs store-name"><span style="font-size:27px">Storefronts</span><br><span style="font-size:19px">For</span><br><span style="font-size:29px">Therapists</span></div>

<!-- Footer -->
<div class="abs footer"></div>
<ul class="abs foot-col" style="left:36px"><li>Kidney Pain</li><li>Kidney Stones</li><li>Kidney Disease Symptoms</li><li>Colon Cleanse</li></ul>
<ul class="abs foot-col" style="left:238px;top:995px"><li>Digestive Enzymes</li><li>Digestive Enzymes Supplement</li><li>Healing Principles</li><li>Herbal Remedies</li></ul>
<ul class="abs foot-col" style="left:475px"><li>Herbal Remedies for Anxiety</li><li>Herbal Remedies for Constipation</li><li>Herbal Remedies for Depression</li><li>Herbal Remedies for Menopause</li></ul>
<ul class="abs foot-col" style="left:755px"><li>Bloated Stomach</li><li>Health Shops</li><li>Enzyvia</li><li>What is Mercury Free Dentistry?</li></ul>
<div class="abs foot-links"><span>About Us</span><span>Search Terms</span><span>Advanced Search</span><span>Terms &amp; Conditions</span><span>Privacy Policy</span><span>Contact Us</span></div>

<div class="abs base-rule"></div>
<div class="abs base-mark"></div>
<div class="abs copyright">© 2010 VitaBrook Enterprises. All Rights Reserved.</div>

</body>
</html>
```